4th Generation Family Business Needs a New Card Design!

We are a family owned 4th Generation company. We are based in the Sydney, Australia area and we are desperately in need of a more modern and classy card. We are monumental masons who design, supply & erect lasting memorials throughout cemeteries in Sydney. Our customers are normally in a period of grieving. I have attached logo files that will need to be implemented on the card. Company was established 1935. Australian Owned and Operated. Card needs to be designed to PRINTLY.com specification.

Target Market(s)

Our target market is based upon people that a grieving for family members that have passed away. We also deal with alot of companies that own and operate cemeteries.

Industry/Entity Type

Business

Contact Information for Business Card

Oliver Brantley, Operations Manager, 0417552908, oliver@hollowaystoneworks.com.au
Martin Brantley, Director, 0431906627, martin@hollowaystoneworks.com.au
Phone # 02 9634 2258
Website: www.hollowaystoneworks.com.au
Address: Suite 17, 8 Calloway Lane, East Penrose, Sydney NSW 2290

Font styles to use
Serif
Decorative
Script

Requirements
Must have
• Would like to see the logo nicely implemented with a modern design. Embossed lettering would be a nice additive.

```html
<!DOCTYPE html>
<html lang="en">
<head>
<meta charset="utf-8">
<title>Holloway Stoneworks – Business Card</title>
<link href="https://fonts.googleapis.com/css2?family=Cinzel:wght@400;600&family=Roboto:wght@300;400&display=swap" rel="stylesheet">
<style>
  :root {
    --bg: #3a3330;
    --card: #1c1c1d;
    --card-edge: #262627;
    --gold: #d9a92a;
    --white: #e9e9e9;
    --muted: #c9c9c9;
    --rule: #3a3a3a;
  }
  * { margin: 0; padding: 0; box-sizing: border-box; }
  html, body { width: 1200px; height: 716px; overflow: hidden; }
  body {
    background: var(--bg);
    font-family: "Roboto", Arial, sans-serif;
    position: relative;
  }
  .card {
    position: absolute;
    top: 193px;
    width: 540px;
    height: 330px;
    background: var(--card);
    border: 1px solid var(--card-edge);
    box-shadow: 0 8px 24px rgba(0,0,0,.45);
  }
  .card--front { left: 40px; }
  .card--back { left: 620px; }

  .brand {
    position: absolute;
    display: flex;
    align-items: center;
    gap: 12px;
    font-family: "Cinzel", Georgia, serif;
    font-weight: 400;
    color: var(--white);
    letter-spacing: 1px;
    line-height: 1.1;
  }
  .brand__mark {
    width: 40px; height: 40px;
    border: 2px solid var(--white);
  }
  .card--front .brand { left: 34px; top: 40px; font-size: 26px; }
  .card--back .brand { right: 34px; top: 36px; font-size: 17px; }
  .card--back .brand__mark { width: 30px; height: 30px; }

  .divider {
    position: absolute;
    left: 34px; right: 34px;
    top: 136px;
    height: 1px;
    background: var(--rule);
  }

  .person {
    position: absolute;
    left: 34px; top: 160px;
  }
  .person__name {
    font-family: "Cinzel", Georgia, serif;
    font-weight: 600;
    font-size: 20px;
    color: var(--gold);
    letter-spacing: .5px;
  }
  .person__role {
    font-size: 12px;
    color: var(--muted);
    margin-top: 2px;
  }

  .contacts {
    position: absolute;
    left: 34px; top: 226px;
    list-style: none;
  }
  .contacts li {
    display: flex;
    align-items: center;
    gap: 8px;
    font-size: 12.5px;
    font-weight: 300;
    color: var(--white);
    height: 19px;
  }
  .contacts svg { width: 11px; height: 11px; fill: var(--gold); flex: none; }

  .address {
    position: absolute;
    right: 34px; top: 160px;
    text-align: right;
    font-size: 12px;
    font-weight: 300;
    color: var(--muted);
    line-height: 1.5;
  }
</style>
</head>
<body>

<section class="card card--front">
  <div class="brand">
    <span class="brand__mark"></span>
    <span>Holloway<br>Stoneworks</span>
  </div>

  <div class="divider"></div>

  <div class="person">
    <p class="person__name">Oliver Brantley</p>
    <p class="person__role">Operations Manager</p>
  </div>

  <ul class="contacts">
    <li>
      <svg viewBox="0 0 12 12"><path d="M3 0h6a1 1 0 0 1 1 1v10a1 1 0 0 1-1 1H3a1 1 0 0 1-1-1V1a1 1 0 0 1 1-1zm0 1.5v8h6v-8z"/></svg>
      0417552908
    </li>
    <li>
      <svg viewBox="0 0 12 12"><path d="M2.5 0.5l2 2.5-1 1.2c.7 1.6 2 2.9 3.6 3.6L8.3 6.8l2.7 2-1 2.4C5 11 1 7 .8 2z"/></svg>
      02 9634 2258
    </li>
    <li>
      <svg viewBox="0 0 12 12"><path d="M0 2h12v8H0zm1 1v.4L6 6.8l5-3.4V3zm0 1.6V9h10V4.6L6 8z"/></svg>
      oliver@hollowaystoneworks.com.au
    </li>
    <li>
      <svg viewBox="0 0 12 12"><path d="M6 0a6 6 0 1 0 0 12A6 6 0 0 0 6 0zm0 1.2c.8.8 1.3 2.3 1.4 4.2H4.6C4.7 3.5 5.2 2 6 1.2zM1.3 6.6h2.2c.1 1.7.5 3 1 3.9A4.8 4.8 0 0 1 1.3 6.6zm0-1.2a4.8 4.8 0 0 1 3.2-3.9c-.5.9-.9 2.2-1 3.9zm3.3 1.2h2.8C7.3 8.5 6.8 10 6 10.8 5.2 10 4.7 8.5 4.6 6.6zm3.9 0h2.2a4.8 4.8 0 0 1-3.2 3.9c.5-.9.9-2.2 1-3.9zm0-1.2c-.1-1.7-.5-3-1-3.9a4.8 4.8 0 0 1 3.2 3.9z"/></svg>
      www.hollowaystoneworks.com.au
    </li>
  </ul>

  <p class="address">Suite 17, 8 Calloway Lane,<br>East Penrose, Sydney NSW 2290</p>
</section>

<section class="card card--back">
  <div class="brand">
    <span class="brand__mark"></span>
    <span>Holloway<br>Stoneworks</span>
  </div>
</section>

</body>
</html>
```